Power Point Template Design for Consulting Company
Verdant Ridge Inc.
Helping Clients Achieve Explosive Sales
Need a slide master incorporating existing logo for all regular Power Point slide layout types (title, title and content, section header, two content, comparison, title only, blank, content with caption, picture with caption)
Corporate client presentations and professional association speaking engagements
Using Power Point 2007, Windows 7.0 O/S.
Not overpowering, prefer clean white backgrounds for better projection and printing results. Verdant Ridge Inc. Logo was designed on a previous project so all files available.
logo files in all formats
business card for reference and consistency
business letterhead for reference and consistency
business stationary coor and font for reference and consistency

```html
<!DOCTYPE html>
<html lang="en">
<head>
<meta charset="utf-8">
<title>Verdant Ridge Inc. – Slide Master</title>
<link rel="stylesheet" href="https://fonts.googleapis.com/css2?family=Exo+2:wght@500&display=swap">
<style>
  :root {
    --band-top: #1e9be0;
    --band-mid: #1470bd;
    --band-bottom: #1d3473;
    --stripe-light: #e6e6e6;
    --stripe-dark: #b9b9b9;
    --paper: #ffffff;
    --paper-shade: #ececec;
    --brand-navy: #1d3f8c;
    --ghost: #d6d6d6;
  }
  html, body {
    margin: 0;
    padding: 0;
    overflow: hidden;
    background: #ffffff;
  }
  .slide {
    position: relative;
    width: 1200px;
    height: 847px;
    overflow: hidden;
    font-family: "Exo 2", sans-serif;
  }
  .slide-frame {
    position: absolute;
    inset: 0;
  }
  .logo-card {
    position: absolute;
    left: 34px;
    top: 29px;
    width: 362px;
    height: 177px;
    background: var(--paper);
    box-shadow: 0 1px 3px rgba(0, 0, 0, 0.12);
  }
  .logo-mark {
    position: absolute;
    left: 45px;
    top: 36px;
    width: 46px;
    height: 46px;
    border-radius: 5px;
    background: var(--band-mid);
  }
  .logo-name {
    position: absolute;
    left: 18px;
    top: 130px;
    margin: 0;
    font-size: 31px;
    font-weight: 500;
    color: var(--brand-navy);
    white-space: nowrap;
    line-height: 1;
  }
  .ghost-mark {
    position: absolute;
    left: 727px;
    top: 384px;
    width: 365px;
    height: 312px;
    border-radius: 26px;
    background: var(--ghost);
    opacity: 0.7;
  }
  .ghost-name {
    position: absolute;
    right: 14px;
    top: 736px;
    margin: 0;
    font-size: 58px;
    font-weight: 500;
    color: var(--ghost);
    white-space: nowrap;
    line-height: 1;
  }
</style>
</head>
<body>
<div class="slide">
  <svg class="slide-frame" width="1200" height="847" viewBox="0 0 1200 847" aria-hidden="true">
    <defs>
      <linearGradient id="band-fill" x1="0" y1="0" x2="0" y2="1">
        <stop offset="0" stop-color="var(--band-top)"/>
        <stop offset="0.45" stop-color="var(--band-mid)"/>
        <stop offset="1" stop-color="var(--band-bottom)"/>
      </linearGradient>
      <linearGradient id="stripe-fill" x1="0" y1="0" x2="1" y2="0">
        <stop offset="0" stop-color="var(--stripe-light)"/>
        <stop offset="1" stop-color="var(--stripe-dark)"/>
      </linearGradient>
      <radialGradient id="paper-fill" cx="0.55" cy="0.3" r="0.9">
        <stop offset="0" stop-color="var(--paper)"/>
        <stop offset="1" stop-color="var(--paper-shade)"/>
      </radialGradient>
    </defs>
    <rect class="side-band" x="0" y="0" width="122" height="847" fill="url(#band-fill)"/>
    <rect class="corner-accent" x="1040" y="0" width="160" height="140" fill="url(#band-fill)"/>
    <path class="content-paper" d="M150 0 H1100 A100 100 0 0 1 1200 100 V847 H150 Z" fill="url(#paper-fill)"/>
    <rect class="side-stripe" x="132" y="0" width="18" height="847" fill="url(#stripe-fill)"/>
  </svg>

  <div class="logo-card">
    <span class="logo-mark"></span>
    <p class="logo-name">Verdant Ridge Inc.</p>
  </div>

  <span class="ghost-mark"></span>
  <p class="ghost-name">Verdant Ridge Inc.</p>
</div>
</body>
</html>
```